"Breathe & Bloom" Book Cover 5.5x8.5

Title of the book is "Breathe & Bloom"
Subtitle is "Unmasking Pricing Myths"
I've used PixelGuild on multiple occasions you can look on my Borvex page, Mark Delwitt, to see the covers I've used in the other projects I've done.
The target audience are people who have been tricked to think they can't retire because inflation, i.e. cost of living is going up so much they must work to keep up. There is no evidence of this.
And those are the people I want to reach so they can "Breathe...and Bloom."
Target Market(s)
Americans aged 55 and over who are thinking about retirement
Industry/Entity Type
Financial
Requirements
Nice to have
- Keep It Simple, Stupid is my mantra. Just make it pop out when people are browsing
Should not have
- No piggy banks. No old people sitting on a beach.

```html
<!DOCTYPE html>
<html lang="en">
<head>
<meta charset="utf-8">
<title>Breathe &amp; Bloom — Book Cover</title>
<link rel="stylesheet" href="https://fonts.googleapis.com/css2?family=Quicksand:wght@300;400&family=Roboto+Condensed:wght@500&display=swap">
<style>
  :root {
    --backdrop: #323135;
    --cover-blue: #4152a0;
    --accent-teal: #00bfa5;
    --ink-white: #ffffff;
    --figure-tone: #5564ad;
  }
  * { margin: 0; padding: 0; box-sizing: border-box; }
  html, body {
    width: 1200px;
    height: 1177px;
    overflow: hidden;
    background: var(--backdrop);
  }
  .canvas {
    position: relative;
    width: 1200px;
    height: 1177px;
    background: var(--backdrop);
  }
  .book-cover {
    position: absolute;
    left: 346px;
    top: 161px;
    width: 548px;
    height: 848px;
    background: var(--cover-blue);
    overflow: hidden;
  }
  .title {
    position: absolute;
    right: 48px;
    top: 42px;
    font-family: "Quicksand", sans-serif;
    font-weight: 300;
    font-size: 96px;
    line-height: 112px;
    color: var(--ink-white);
    text-align: left;
  }
  .title-line { display: block; }
  .title-line--first { margin-left: 0; }
  .title-line--second { margin-left: -60px; }
  .ampersand { color: var(--accent-teal); }
  .title-wrap {
    position: absolute;
    left: 50px;
    top: 40px;
    width: 450px;
    font-family: "Quicksand", sans-serif;
    font-weight: 300;
    font-size: 96px;
    line-height: 112px;
    color: var(--ink-white);
  }
  .title-wrap .title-line--first { padding-left: 0; }
  .title-wrap .title-line--second { padding-left: 55px; }
  .subtitle {
    position: absolute;
    left: 116px;
    top: 284px;
    width: 390px;
    font-family: "Quicksand", sans-serif;
    font-weight: 400;
    font-size: 30px;
    color: var(--accent-teal);
    white-space: nowrap;
  }
  .figures-art {
    position: absolute;
    left: 182px;
    top: 493px;
    width: 240px;
    height: 208px;
  }
  .ground-line {
    position: absolute;
    left: 0;
    top: 700px;
    width: 100%;
    height: 2px;
    background: var(--ink-white);
  }
  .base-band {
    position: absolute;
    left: 0;
    bottom: 0;
    width: 100%;
    height: 133px;
    background: var(--accent-teal);
  }
  .author {
    position: absolute;
    right: 28px;
    bottom: 18px;
    font-family: "Roboto Condensed", sans-serif;
    font-weight: 500;
    font-size: 36px;
    color: var(--cover-blue);
  }
</style>
</head>
<body>
  <main class="canvas">
    <section class="book-cover">
      <h1 class="title-wrap">
        <span class="title-line title-line--first">Breathe</span>
        <span class="title-line title-line--second"><span class="ampersand">&amp;</span> Bloom</span>
      </h1>
      <p class="subtitle">Unmasking Pricing Myths</p>
      <svg class="figures-art" role="img" aria-label="Single-line drawing of a couple seen from behind, sitting side by side" viewBox="0 0 240 208">
        <rect x="0" y="0" width="240" height="208" rx="40" fill="var(--figure-tone)"/>
      </svg>
      <div class="ground-line"></div>
      <div class="base-band">
        <p class="author">Mark Delwitt</p>
      </div>
    </section>
  </main>
</body>
</html>
```